Business Card Design

I need a business card for my baking business. Name of the company is Whisked by Tessa. I specialize in cookies and pies.
I don't make cupcakes or cakes. I would like a design with colors of brown, light pink and dark pink and maybe have the half eaten cookie be the dot of the "I" in my name. (Half eaten chocolate chip and the chips being hot pink light pink and brown chips).. I would like the card fun and modern design.
On the back of the card tag line- let me bake your day

Industry/Entity Type

Business

Contact Information for Business Card

Tessa Mernholt
Cell 5093617284
Email-Tesmern47@quillpost.net

```html
<!DOCTYPE html>
<html lang="en">
<head>
<meta charset="utf-8">
<title>Whisked by Tessa — Business Card</title>
<link rel="stylesheet" href="https://fonts.googleapis.com/css2?family=Noto+Sans:wght@400;700;800&display=swap">
<style>
  :root {
    --stage: #24262b;
    --cocoa: #4a2b16;
    --cocoa-deep: #3a2110;
    --blush: #ee94b9;
    --ink: #3b2414;
    --paper: #ffffff;
  }
  * { box-sizing: border-box; margin: 0; padding: 0; }
  html, body {
    width: 1200px; height: 900px; overflow: hidden;
    background: var(--stage);
    font-family: "Noto Sans", Verdana, sans-serif;
  }
  .sheet {
    width: 1200px; height: 900px;
    display: flex; flex-direction: column; align-items: center; justify-content: center;
    gap: 40px;
  }
  .card {
    width: 660px; height: 377px; position: relative; overflow: hidden;
    box-shadow: 0 10px 30px rgba(0,0,0,.45);
  }

  /* Back side */
  .card--back { background: var(--cocoa); }
  .card--back .cookie-pattern {
    position: absolute; inset: 0;
    background: radial-gradient(circle at 50% 50%, var(--cocoa) 0%, var(--cocoa-deep) 100%);
  }
  .tagline {
    position: absolute; inset: 0;
    display: flex; align-items: center; justify-content: center;
    color: var(--blush); font-weight: 700; font-size: 26px; letter-spacing: .5px;
  }

  /* Front side */
  .card--front { background: var(--paper); }
  .wordmark {
    position: absolute; left: 48px; top: 88px;
    display: flex; align-items: flex-start; gap: 8px;
  }
  .wordmark__name {
    color: var(--blush); font-weight: 800; font-size: 96px; line-height: 1;
    letter-spacing: 2px; text-transform: uppercase;
  }
  .wordmark__cookie {
    width: 34px; height: 34px; border-radius: 50%;
    background: #b89572; margin-top: -6px;
  }
  .company {
    position: absolute; left: 48px; bottom: 40px;
    color: var(--ink); font-weight: 700; font-size: 28px;
  }
  .contact {
    position: absolute; right: 40px; top: 150px;
    display: flex; flex-direction: column; gap: 6px;
  }
  .contact__name { color: var(--blush); font-weight: 700; font-size: 22px; margin-bottom: 2px; }
  .contact__line {
    display: flex; align-items: center; gap: 8px;
    color: var(--ink); font-size: 15px;
  }
  .contact__icon { width: 16px; height: 16px; flex: none; }
</style>
</head>
<body>
<main class="sheet">
  <section class="card card--back" aria-label="Card back">
    <div class="cookie-pattern" role="img" aria-label="Faint repeating pattern of bitten chocolate chip cookies"></div>
    <p class="tagline">let me bake your day</p>
  </section>

  <section class="card card--front" aria-label="Card front">
    <div class="wordmark">
      <span class="wordmark__name">Tessa</span>
      <span class="wordmark__cookie" role="img" aria-label="Half eaten chocolate chip cookie illustration"></span>
    </div>
    <p class="company">Whisked by Tessa</p>
    <div class="contact">
      <p class="contact__name">Tessa Mernholt</p>
      <p class="contact__line">
        <svg class="contact__icon" viewBox="0 0 16 16" aria-hidden="true">
          <rect x="1" y="1" width="14" height="14" rx="2" fill="var(--blush)"/>
          <rect x="5" y="3" width="6" height="10" rx="1" fill="none" stroke="#fff" stroke-width="1.3"/>
          <circle cx="8" cy="11" r=".8" fill="#fff"/>
        </svg>
        5093617284
      </p>
      <p class="contact__line">
        <svg class="contact__icon" viewBox="0 0 16 16" aria-hidden="true">
          <rect x="1" y="1" width="14" height="14" rx="2" fill="var(--blush)"/>
          <rect x="3.5" y="5" width="9" height="6.5" fill="none" stroke="#fff" stroke-width="1.2"/>
          <path d="M3.5 5 L8 9 L12.5 5" fill="none" stroke="#fff" stroke-width="1.2"/>
        </svg>
        Tesmern47@quillpost.net
      </p>
    </div>
  </section>
</main>
</body>
</html>
```